Coffee Pouch Label for Coffee Roaster

We are wanting some new labels for our coffee pouches.
We are an established, small family owned specialty coffee roaster called Tallow Creek Coffee Roasters, and we are located in Yass, NSW Australia.
Label dimensions are 100 x 150mm, to fit on a couple of different bag sizes. We use coffee pouches with kraft paper finish.
We have 3 main blends, Marigold, Lanternfly & Slow Tide, and a range of rotating single origin coffees. We would get labels printed for the blends, but then need a 'generic' design that we can either write the name on, or stick another sticker over for the single origin coffees.
Some information that needs to be on the label:
our logo
web address: www.tallowcreekcoffee.example
address: 47 Garrick St, Yass, NSW
Proudly Roasted in Yass, NSW
Blend name
our tagline/mission: act justly | love mercy | walk humbly
statement: we give $1 from every kg of coffee sold to the rescue, prevention and rehabilitation of children from slavery.
We would like to use colour to help differentiate the different blends somehow.
We are after a creative, clean design, that is representative of specialty coffee (not large commercial coffee brands).
I have uploaded our logo both with and without our tagline, and also some other packaging inspiration that i like (I quite like the meadow coffee label design).
thanks everyone!
Rupert
People who appreciate good, local coffee

```html
<!DOCTYPE html>
<html lang="en">
<head>
<meta charset="utf-8">
<title>Tallow Creek Coffee Roasters – Blend Labels</title>
<link rel="stylesheet" href="https://fonts.googleapis.com/css2?family=PT+Sans:wght@700&family=Alegreya:wght@500&family=Montserrat:wght@500;700&family=Work+Sans:wght@400;600&display=swap">
<style>
  :root {
    --ink: #2a2a2b;
    --paper: #ffffff;
    --rule: #2a2a2b;
    --footer-band: #2b2b2c;
    --footer-text: #454547;
    --marigold: #e9bdd9;
    --lanternfly: #c2dbc6;
    --slow-tide: #b4b4b7;
    --ghost: rgba(200, 200, 202, 0.55);
    --label-w: 366px;
    --label-h: 548px;
  }
  * { box-sizing: border-box; margin: 0; padding: 0; }
  html, body {
    width: 1200px;
    height: 610px;
    overflow: hidden;
    background: var(--paper);
  }
  .sheet {
    position: relative;
    width: 1200px;
    height: 610px;
  }
  .label {
    position: absolute;
    top: 32px;
    width: var(--label-w);
    height: var(--label-h);
    border: 1px solid var(--ink);
    background: var(--paper);
    overflow: hidden;
    color: var(--ink);
    text-align: center;
  }
  .label--marigold { left: 33px; }
  .label--lanternfly { left: 419px; }
  .label--slow-tide { left: 801px; }

  .label__colour-field {
    position: absolute;
    inset: 0;
    width: 100%;
    height: 100%;
  }
  .label--marigold .label__colour-field polygon { fill: var(--marigold); }
  .label--lanternfly .label__colour-field polygon { fill: var(--lanternfly); }
  .label--slow-tide .label__colour-field polygon { fill: var(--slow-tide); }

  .label__backdrop-art {
    position: absolute;
    left: 0;
    top: 50px;
    width: 180px;
    height: 190px;
    background: radial-gradient(ellipse at 45% 50%, var(--ghost) 0%, rgba(220,220,222,0.25) 55%, rgba(255,255,255,0) 75%);
  }

  .label__content {
    position: absolute;
    inset: 0;
  }
  .line {
    position: absolute;
    left: 0;
    right: 0;
  }
  .tagline {
    top: 50px;
    font-family: 'PT Sans', sans-serif;
    font-weight: 700;
    font-size: 16.5px;
    letter-spacing: 0.1px;
  }
  .brand-name {
    top: 128px;
    left: 70px;
    right: 70px;
    font-family: 'PT Sans', sans-serif;
    font-weight: 700;
    font-size: 26px;
    line-height: 1.05;
    color: var(--ink);
  }
  .origin {
    top: 221px;
    font-family: 'Alegreya', serif;
    font-weight: 500;
    font-size: 11.2px;
  }
  .blend-kicker {
    top: 253px;
    display: flex;
    justify-content: center;
    align-items: center;
    gap: 6px;
    font-family: 'Montserrat', sans-serif;
    font-weight: 500;
    font-size: 15px;
    line-height: 1;
  }
  .blend-kicker::before,
  .blend-kicker::after {
    content: "";
    width: 42px;
    height: 2px;
    background: var(--rule);
  }
  .blend-name {
    top: 270px;
    font-family: 'Montserrat', sans-serif;
    font-weight: 700;
    font-size: 25px;
    letter-spacing: 0.4px;
  }
  .blend-illustration {
    position: absolute;
    top: 320px;
    left: 50%;
    width: 84px;
    height: 74px;
    transform: translateX(-50%);
    border-radius: 50%;
    background: radial-gradient(circle, rgba(42,42,43,0.85) 0%, rgba(42,42,43,0.55) 45%, rgba(42,42,43,0) 72%);
  }
  .mission {
    top: 420px;
    left: 40px;
    right: 40px;
    font-family: 'Alegreya', serif;
    font-weight: 500;
    font-size: 11.6px;
    line-height: 1.38;
    letter-spacing: 0.2px;
  }
  .net-weight {
    top: 475px;
    font-family: Arial, 'Helvetica Neue', sans-serif;
    font-weight: 700;
    font-size: 18px;
  }
  .net-weight small { font-size: 14px; }
  .footer {
    top: 509px;
    font-family: 'Work Sans', sans-serif;
    font-size: 11.4px;
    line-height: 1.35;
    color: var(--footer-text);
    letter-spacing: 0.2px;
  }
  .footer__web { font-weight: 600; color: var(--ink); letter-spacing: 0.6px; }
  .footer-band {
    position: absolute;
    left: 0; right: 0; bottom: 0;
    height: 47px;
    background: var(--footer-band);
  }
  .label--marigold .footer,
  .label--marigold .footer__web { color: #ffffff; }
</style>
</head>
<body>
<main class="sheet">

  <!-- Marigold -->
  <article class="label label--marigold">
    <svg class="label__colour-field" viewBox="0 0 366 548" preserveAspectRatio="none" aria-hidden="true">
      <polygon points="366,0 366,548 0,548 0,501"/>
    </svg>
    <div class="label__backdrop-art" role="img" aria-label="Faint engraved coffee branch with cherries and leaves"></div>
    <div class="footer-band"></div>
    <div class="label__content">
      <p class="line tagline">Act Justly | Love Mercy | Walk Humbly</p>
      <p class="line brand-name">Tallow Creek Coffee Roasters</p>
      <p class="line origin">Proudly Roasted In Yass, NEW SOUTH WALES</p>
      <p class="line blend-kicker">BLEND</p>
      <h2 class="line blend-name">MARIGOLD</h2>
      <div class="blend-illustration" role="img" aria-label="Engraved coffee branch with cherries"></div>
      <p class="line mission">“we give $1 from every kg of coffee sold to the rescue, prevention, and rehabilitation of childrten from slavery.”</p>
      <p class="line net-weight">250 <small>g</small></p>
      <p class="line footer">Tallow Creek Coffee Roasters | 47 Garrick St, Yass, NSW<br><span class="footer__web">www.tallowcreekcoffee.example</span></p>
    </div>
  </article>

  <!-- Lanternfly -->
  <article class="label label--lanternfly">
    <svg class="label__colour-field" viewBox="0 0 366 548" preserveAspectRatio="none" aria-hidden="true">
      <polygon points="366,0 366,548 0,548"/>
    </svg>
    <div class="label__backdrop-art" role="img" aria-label="Faint engraved pair of roasted coffee beans"></div>
    <div class="label__content">
      <p class="line tagline">Act Justly | Love Mercy | Walk Humbly</p>
      <p class="line brand-name">Tallow Creek Coffee Roasters</p>
      <p class="line origin">Proudly Roasted In Yass, NEW SOUTH WALES</p>
      <p class="line blend-kicker">BLEND</p>
      <h2 class="line blend-name">LANTERNFLY</h2>
      <div class="blend-illustration" role="img" aria-label="Engraved pair of roasted coffee beans"></div>
      <p class="line mission">“we give $1 from every kg of coffee sold to the rescue, prevention, and rehabilitation of childrten from slavery.”</p>
      <p class="line net-weight">250 <small>g</small></p>
      <p class="line footer">Tallow Creek Coffee Roasters | 47 Garrick St, Yass, NSW<br><span class="footer__web">www.tallowcreekcoffee.example</span></p>
    </div>
  </article>

  <!-- Slow Tide -->
  <article class="label label--slow-tide">
    <svg class="label__colour-field" viewBox="0 0 366 548" preserveAspectRatio="none" aria-hidden="true">
      <polygon points="366,0 366,548 0,548"/>
    </svg>
    <div class="label__backdrop-art" role="img" aria-label="Faint engraved coffee cup on a cloth with scattered beans"></div>
    <div class="label__content">
      <p class="line tagline">Act Justly | Love Mercy | Walk Humbly</p>
      <p class="line brand-name">Tallow Creek Coffee Roasters</p>
      <p class="line origin">Proudly Roasted In Yass, NEW SOUTH WALES</p>
      <p class="line blend-kicker">BLEND</p>
      <h2 class="line blend-name">SLOW TIDE</h2>
      <div class="blend-illustration" role="img" aria-label="Engraved coffee cup on a cloth with scattered beans"></div>
      <p class="line mission" style="top:422px">“we give $1 from every kg of coffee sold to the rescue, prevention, and rehabilitation of childrten from slavery.”</p>
      <p class="line net-weight">250 <small>g</small></p>
      <p class="line footer">Tallow Creek Coffee Roasters | 47 Garrick St, Yass, NSW<br><span class="footer__web">www.tallowcreekcoffee.example</span></p>
    </div>
  </article>

</main>
</body>
</html>
```